依頼詳細
PCとスマホデザインの両方納品をいただきますが、
まずはデザインイメージが確認しやすいPCページのみの提案をお願いします。
スマホページは当選者に納品時にお願いしたいと思います。
スマホサイズについて、カンバスサイズは横幅375pxで作成し、2倍の横幅750pxのサイズで書き出ししてください。
(Retinaディスプレイに対応するため)
スマホページ作成時は、メニューが展開した際のデザインもお願いします。
レスポンシブウェブデザインを意識したデザインでお願いします。

■サイトマップ
添付の画面遷移図をご確認ください。

■参考サイト
https://www.hirotoku-sarumi.jp/
https://www.tabuse-seiban.co.jp/

■内容について
主に鋼材の卸売業を行う会社の公式サイトになります。
卸売だけでなく、鋼板を仕入れて希望のサイズに切断、プレスなどの加工も行う会社です。
参考サイトはメインビジュアルが動画になっていますが、今回のサイトデザインでは動画を使用する予定は今のところありません。

■素材写真
画像データについては、フリー素材から流用して
イメージ画像に当て込んでください。
足りない場合は、一旦他のサイトの写真をサンプルとして
入れてください。(サンプルなどの表記をお願いします)
また、購入が必要な写真などを利用した場合、
価格とサイト名を教えてください。

また、Pixoral Imageで定期契約をしていますので、
Pixoral Imageの画像は使用できます。
デザイン時はカンプ画像をお入れいただきますようお願いします。

■ロゴについて
添付のロゴデータを使用してください。

■ワイヤーフレーム
https://mock.velqara.net/view/52817caa-1f3b-4d0e-9a72-6e1b8c37d904-b39f/?fullscreen
コンテンツの構成としてワイヤーフレームを作成しましたが
必ずしもワイヤーフレームの通りではなくて大丈夫です。
TOPページに配置するコンテンツを見ていただき、デザインは
デザイナーの皆様におまかせしたいと思います。

----------------------------------------------------------------------------
【制作物に対するお願い】

■フォントについて
・無料で使えるフォントで作成をお願いします。
・OSに紐づくフォントの使用は控えていただければと思います (ヒラギノなど)

ページ数
1ページ
希望イメージ
シンプル 複雑
単色 カラフル
暗い 明るい
日常 高級
遊び心 厳粛
未来的 伝統的
女性的 男性的
希望する色
ベースカラー:白、青、ポイントカラー:赤
納品ファイル
• 高解像度JPG (.jpg)
• イラストレーター形式 (.ai)
• フォトショップ形式 (.psd)
補足説明
上記のいずれか1つ(アウトラインありとなしの2つ)と高解像度JPGを納品お願いします。
adobe XDでの納品も可能です。
CS5にバージョンを落としたロゴデータです。
ロゴのpngデータも追加しました。

```html
<!DOCTYPE html>
<html lang="ja">
<head>
<meta charset="utf-8">
<title>北嶺スチール株式会社</title>
<link rel="stylesheet" href="https://fonts.googleapis.com/css2?family=Noto+Sans+JP:wght@400;500;700;900&family=Oswald:wght@500;600&display=swap">
<style>
:root{
  --blue:#1a4fb4;
  --blue-dark:#123a8a;
  --red:#d7201f;
  --ink:#1d1d1f;
  --text:#444;
  --grey-bg:#efeff1;
  --footer-bg:#f3f3f5;
  --white:#fff;
}
*{margin:0;padding:0;box-sizing:border-box}
html,body{width:1200px;height:3444px;overflow:hidden}
body{position:relative;background:var(--white);font-family:"Noto Sans JP",sans-serif;color:var(--ink)}
.abs{position:absolute}
.brand{font-weight:900;font-size:26px;color:var(--red);display:flex;align-items:center;gap:10px;letter-spacing:1px}
.brand .mark{width:14px;height:14px;background:var(--red)}
.site-header{left:0;top:0;width:1200px;height:100px;background:var(--white)}
.site-header .brand{position:absolute;left:120px;top:32px}
.nav{position:absolute;left:628px;top:40px;display:flex;gap:30px;font-size:15px;font-weight:500}
.header-cta{position:absolute;right:0;top:0;width:186px;height:80px;background:var(--blue);color:#fff;font-size:15px;display:flex;align-items:center;justify-content:center}
.photo{background:linear-gradient(135deg,#3b4650,#22282f 55%,#4a5560)}
.hero{left:0;top:100px;width:1200px;height:660px;background:radial-gradient(circle at 38% 70%,#f3a54a 0,#8a5a30 10%,transparent 26%),linear-gradient(120deg,#6f7a72,#2d3632 50%,#2f5a4e)}
.about-bg{left:0;top:760px;width:1200px;height:1210px;background:var(--grey-bg)}
.card{background:var(--white);padding:72px 80px 0}
.sec-title{font-family:"Oswald",sans-serif;font-weight:600;font-size:54px;line-height:1;border-left:6px solid var(--red);padding-left:16px;letter-spacing:1px}
.sec-sub{font-size:15px;font-weight:500;margin:12px 0 0 22px}
.lead{font-size:17px;font-weight:700;margin-top:38px}
.body-text{font-size:12px;line-height:2.1;color:var(--text);margin-top:20px;letter-spacing:.5px}
.btns{display:flex;gap:28px;margin-top:44px}
.btn{width:190px;height:62px;background:var(--blue);color:#fff;font-size:14px;display:flex;align-items:center;justify-content:center;gap:14px}
.about{left:120px;top:732px;width:700px;height:520px}
.welder{left:80px;top:1348px;width:368px;height:552px;background:linear-gradient(160deg,#c9cdd0,#8e9298 60%,#b45a36)}
.sparks{left:472px;top:1300px;width:728px;height:488px;background:radial-gradient(circle at 48% 55%,#9fd2ff 0,#3d6fb0 12%,transparent 34%),linear-gradient(120deg,#2b3035,#111519)}
.team{left:0;top:1972px;width:1200px;height:668px;background:linear-gradient(180deg,#8c979f,#4d5763 55%,#2b3a5a)}
.recruit{left:440px;top:2520px;width:760px;height:520px}
.site-footer{left:0;top:3080px;width:1200px;height:364px;background:var(--footer-bg)}
.foot-brand{left:150px;top:3130px}
.address{left:150px;top:3178px;font-size:12px;line-height:1.9;color:var(--text)}
.tel-box{left:460px;top:3136px;width:430px;height:104px;border:3px solid var(--blue);background:#fff;padding:14px 22px}
.tel-box small{display:block;font-size:12px;color:var(--text)}
.tel{font-family:"Oswald",sans-serif;font-size:38px;font-weight:600;color:var(--blue);display:flex;align-items:center;gap:10px;line-height:1.2}
.tel-hours{font-size:12px;color:var(--text)}
.mail-box{left:890px;top:3136px;width:160px;height:104px;background:var(--blue);color:#fff;font-size:13px;display:flex;flex-direction:column;align-items:center;justify-content:center;gap:10px}
.foot-nav{left:150px;top:3302px;display:flex;gap:24px;font-size:13px}
.copyright{left:0;top:3386px;width:1200px;text-align:center;font-size:11px;color:#777}
</style>
</head>
<body>
<header class="abs site-header">
  <div class="brand"><span class="mark"></span>北嶺スチール株式会社</div>
  <nav class="nav"><span>事業内容</span><span>会社概要</span><span>採用情報</span></nav>
  <div class="header-cta">お問い合わせ</div>
</header>

<div class="abs hero" role="img" aria-label="作業服の職人がグラインダーで鋼材を加工し火花が散る工場の写真"></div>
<div class="abs about-bg"></div>

<section class="abs card about">
  <h2 class="sec-title">ABOUT</h2>
  <p class="sec-sub">北嶺スチールについて</p>
  <p class="lead">テキストが入りますテキストが入ります</p>
  <p class="body-text">鋼材の仕入れから切断、プレス加工まで一貫して対応しています。お客様のご要望に合わせた最適なサイズと品質をお届けし、地域のものづくりを支え続けます。確かな技術と迅速な対応で、信頼されるパートナーを目指しています。</p>
  <p class="body-text">長年培った経験を活かし、多様な業界のニーズに応える体制を整えています。</p>
  <div class="btns">
    <div class="btn">事業内容 <svg width="18" height="10" viewBox="0 0 18 10"><path d="M0 5h16M12 1l4 4-4 4" stroke="#fff" fill="none" stroke-width="1.5"/></svg></div>
    <div class="btn">会社概要 <svg width="18" height="10" viewBox="0 0 18 10"><path d="M0 5h16M12 1l4 4-4 4" stroke="#fff" fill="none" stroke-width="1.5"/></svg></div>
  </div>
</section>

<div class="abs sparks" role="img" aria-label="暗い工場で溶接の青白い光と火花が広がる写真"></div>
<div class="abs welder" role="img" aria-label="溶接面を持った若い作業員の写真"></div>

<div class="abs team" role="img" aria-label="工場内で紺色の作業服を着て並ぶ社員たちの写真"></div>

<section class="abs card recruit">
  <h2 class="sec-title">RECRUIT</h2>
  <p class="sec-sub">採用情報</p>
  <p class="lead">テキストが入りますテキストが入ります</p>
  <p class="body-text">私たちと一緒に、鉄でまちの未来をつくりませんか。未経験の方も先輩社員が丁寧にサポートします。資格取得の支援制度も充実しており、成長できる環境が整っています。</p>
  <p class="body-text">働きやすい職場づくりに取り組み、長く安心して働ける会社です。</p>
  <div class="btns">
    <div class="btn">採用情報 <svg width="18" height="10" viewBox="0 0 18 10"><path d="M0 5h16M12 1l4 4-4 4" stroke="#fff" fill="none" stroke-width="1.5"/></svg></div>
  </div>
</section>

<footer class="abs site-footer"></footer>
<div class="abs brand foot-brand"><span class="mark"></span>北嶺スチール株式会社</div>
<p class="abs address">〒955-0000 新潟県三条市中央町1-2-3<br>TEL：0256-71-5032<br>FAX：0256-71-5039</p>
<div class="abs tel-box">
  <small>ご相談やご依頼など、お気軽にお問い合わせください</small>
  <div class="tel"><svg width="28" height="28" viewBox="0 0 24 24"><path fill="#1a4fb4" d="M6.6 10.8a15 15 0 0 0 6.6 6.6l2.2-2.2c.3-.3.7-.4 1-.2 1.1.4 2.3.6 3.6.6.6 0 1 .4 1 1V20c0 .6-.4 1-1 1A17 17 0 0 1 3 4c0-.6.4-1 1-1h3.5c.6 0 1 .4 1 1 0 1.3.2 2.5.6 3.6.1.3 0 .7-.2 1z"/></svg>0256-71-5032</div>
  <p class="tel-hours">受付時間：9：00〜17：00（土日祝除く）</p>
</div>
<div class="abs mail-box">お問い合わせ<svg width="40" height="28" viewBox="0 0 40 28"><rect x="1" y="1" width="38" height="26" fill="#fff"/><path d="M1 1l19 15L39 1" stroke="#1a4fb4" stroke-width="2" fill="none"/></svg></div>
<nav class="abs foot-nav"><span>TOPページ</span><span>事業内容</span><span>会社概要</span><span>採用情報</span><span>お問い合わせ</span><span>プライバシーポリシー</span><span>サイトポリシー</span></nav>
<p class="abs copyright">Copyright © 北嶺スチール株式会社 All Rights Reserved.</p>
</body>
</html>
```